Robotic startup business cards

We are looking for a design for a set of business cards which reflect the spirit and humor of Vortalo Robotics. We want to present ourselves as sleek, professional, but laid-back consulting company.

We primarily focus on developing robotic arms software. This software controls robots and does things like grab items, pick objects up, move them, etc.

We want to allow you maximum design creativity, but do ask that you consider our existing style guidelines (see attached files) in order to make our brand cohesive.

Target Market(s)

Startups and Mid-size robotic companies

Industry/Entity Type

Business

Contact Information for Business Card

Miro Halvensky, PhD
Roboticist | Vortalo Consulting | 318.570.9164

Font styles to use
Other font styles liked:
• Source code pro

Requirements
Must have
• robots or robotic arms
• similar color scheme that works with existing brand guidelines
Nice to have
• please consider our existing style guidelines (see attached files) in order to make our brand cohesive.
• minimalism style is generally nice.
Should not have
• An old, boring, or corporate feel. Too much text.

```html
<!DOCTYPE html>
<html lang="en">
<head>
<meta charset="utf-8">
<title>Vortalo Robotics – Business Cards</title>
<link rel="stylesheet" href="https://fonts.googleapis.com/css2?family=Source+Code+Pro:wght@300;400;600;700&display=swap">
<style>
  :root {
    --bg: #e9e6e1;
    --card-dark: #0b0c0d;
    --card-dark-2: #1c1e20;
    --card-light: #f6f6f6;
    --card-light-2: #dcdcdc;
    --brand-green: #5ec99a;
    --ink: #2a2a2a;
    --ink-soft: #3c3c3c;
    --wordmark-light: #e4e4e4;
    --swoosh-dark: #232323;
    --swoosh-grey: #cfcfcf;
    --arm-1: #f2f3f5;
    --arm-2: #9aa0a8;
  }
  * { box-sizing: border-box; margin: 0; padding: 0; }
  html, body {
    width: 1200px; height: 784px; overflow: hidden;
    background: var(--bg);
    font-family: "Source Code Pro", monospace;
  }
  .canvas { position: relative; width: 1200px; height: 784px; }

  .card {
    position: absolute; width: 640px; height: 366px;
    border-radius: 4px; overflow: hidden;
    box-shadow: 0 14px 30px rgba(0,0,0,.22);
  }

  /* Front */
  .card--front {
    left: 100px; top: 40px;
    background: linear-gradient(135deg, var(--card-dark-2) 0%, var(--card-dark) 55%, var(--card-dark-2) 100%);
    display: flex; align-items: center; justify-content: center;
  }
  .brand { display: flex; align-items: center; gap: 22px; }
  .brand__square {
    width: 46px; height: 46px; border-radius: 6px;
    background: var(--brand-green);
  }
  .brand__name {
    font-weight: 300; letter-spacing: .22em;
    color: var(--wordmark-light); font-size: 40px;
  }

  /* Back */
  .card--back {
    left: 460px; top: 378px;
    background: linear-gradient(160deg, var(--card-light) 0%, var(--card-light-2) 100%);
  }
  .card--back .brand { position: absolute; left: 58px; top: 92px; gap: 20px; }
  .card--back .brand__square { width: 52px; height: 52px; }
  .card--back .brand__name { color: var(--ink); font-size: 38px; }

  .robot-arm {
    position: absolute; right: 0; top: 0; width: 250px; height: 230px;
    background: radial-gradient(ellipse at 60% 40%, var(--arm-1) 0%, var(--arm-2) 70%, transparent 72%);
  }

  .contact { position: absolute; left: 168px; top: 196px; text-align: center; }
  .contact__name {
    color: var(--brand-green); font-weight: 600; font-size: 24px; letter-spacing: .04em;
  }
  .contact__name small { font-size: 13px; vertical-align: 6px; }
  .contact__role {
    color: var(--ink-soft); font-weight: 700; font-size: 11px; letter-spacing: .06em; line-height: 1.35;
  }
  .contact__phone {
    margin-top: 16px; color: var(--ink); font-weight: 400; font-size: 25px; letter-spacing: .04em;
  }

  .swooshes { position: absolute; left: 0; bottom: 0; width: 640px; height: 366px; }
</style>
</head>
<body>
<main class="canvas">

  <section class="card card--front" aria-label="Card front">
    <div class="brand">
      <span class="brand__square"></span>
      <span class="brand__name">VORTALO</span>
    </div>
  </section>

  <section class="card card--back" aria-label="Card back">
    <svg class="swooshes" viewBox="0 0 640 366" aria-hidden="true">
      <path d="M0 345 C180 320 360 250 500 220 C560 206 610 205 640 210 L640 222 C600 218 560 222 500 236 C360 268 200 335 0 362 Z" fill="var(--brand-green)"/>
      <path d="M420 300 C500 280 580 250 640 190 L640 260 C590 280 500 300 420 300 Z" fill="var(--swoosh-grey)"/>
      <path d="M470 262 C560 250 610 220 640 175 L640 190 C600 236 540 262 470 262 Z" fill="var(--swoosh-dark)"/>
      <path d="M0 366 C200 340 380 300 640 290 L640 366 Z" fill="#ffffff" opacity=".55"/>
    </svg>

    <div class="robot-arm" role="img" aria-label="Photo of a white robotic arm with an open gripping hand reaching down"></div>

    <div class="brand">
      <span class="brand__square"></span>
      <span class="brand__name">VORTALO</span>
    </div>

    <div class="contact">
      <p class="contact__name">MIRO HALVENSKY,<small>PHD</small></p>
      <p class="contact__role">ROBOTICIST<br>VORTALO CONSULTING</p>
      <p class="contact__phone">318.570.9164</p>
    </div>
  </section>

</main>
</body>
</html>
```